Counselling business requires poster

I require a poster to promote my counselling and coaching business I will be placing these in doctors surgery's and clinics etc.
This business is centred around helping people work through emotional issues. We provided one on one sessions which help enhance peoples lives by assisting them in overcoming their fears, obsessions, insecurities etc.

We offer support in a broad range of areas:

- Eating disorders & weight managment
- Depression
- Marriage and relationship issues
- Anxiety
- Victims of physical, verbal and/or social abuse

We want our poster to be representative of the positive, warm and welcoming atmosphere we provide.

Our motto, 'One step at a time', is symbolic of our approach and how we help our clients to tackle their problems bit by bit.

The flyer I have uploaded is just some information on what we offer

Thankyou for your designs I am taking them into consideration and will inform you of any decision.

```html
<!DOCTYPE html>
<html lang="en">
<head>
<meta charset="UTF-8">
<title>One Step at a Time – Pathways Counselling</title>
<link rel="stylesheet" href="https://fonts.googleapis.com/css2?family=Archivo:wght@700;800&family=Archivo+Black&display=swap">
<style>
  :root {
    --paper: #ffffff;
    --brand-navy: #27307a;
    --rust: #a0583c;
    --plum: #4a3550;
    --bear-warm: #c98f72;
    --bear-cool: #9b8aa0;
  }
  * { margin: 0; padding: 0; box-sizing: border-box; }
  html, body {
    width: 848px;
    height: 1200px;
    overflow: hidden;
    background: var(--paper);
  }
  .poster {
    position: relative;
    width: 848px;
    height: 1200px;
    background: var(--paper);
    font-family: "Archivo", Arial, sans-serif;
  }
  .brand {
    position: absolute;
    top: 18px;
    right: 16px;
    display: flex;
    align-items: center;
    gap: 8px;
    font-family: "Archivo", Arial, sans-serif;
    font-weight: 800;
    font-size: 36px;
    letter-spacing: -0.5px;
    color: var(--brand-navy);
  }
  .brand-dot {
    width: 30px;
    height: 30px;
    border-radius: 50%;
    background: var(--brand-navy);
  }
  .hero-photo {
    position: absolute;
    left: 85px;
    top: 184px;
    width: 685px;
    height: 516px;
    border-radius: 40% 40% 30% 30% / 45% 45% 20% 20%;
    background: linear-gradient(90deg, var(--bear-warm) 0%, #b88a80 48%, var(--bear-cool) 58%, #8f7d96 100%);
    opacity: 0.9;
  }
  .headline {
    font-family: "Archivo Black", "Arial Black", sans-serif;
    line-height: 1;
  }
  .headline span {
    position: absolute;
    white-space: nowrap;
  }
  .word-big {
    font-size: 142px;
    letter-spacing: -0.07em;
    color: var(--rust);
  }
  .word-small {
    font-size: 86px;
    letter-spacing: -0.04em;
    color: var(--plum);
  }
  .word-one  { left: 100px; top: 726px; }
  .word-step { left: 394px; top: 764px; }
  .word-ata  { left: 196px; top: 846px; }
  .word-time { left: 402px; top: 826px; }
  .message {
    position: absolute;
    left: 0;
    width: 848px;
    top: 1004px;
    text-align: center;
    font-weight: 700;
    font-size: 18px;
    line-height: 24px;
    letter-spacing: -0.6px;
    color: var(--plum);
  }
  .message .pledge {
    display: block;
    margin-top: 5px;
    color: var(--rust);
    text-transform: uppercase;
  }
  .message .goal {
    display: block;
    text-transform: uppercase;
  }
</style>
</head>
<body>
  <main class="poster">
    <div class="brand">
      <span class="brand-dot"></span>
      <span class="brand-name">PATHWAYS</span>
    </div>

    <div class="hero-photo" role="img" aria-label="Photograph of two worn, patched teddy bears sitting side by side, a brown bear comforting a grey-purple bear holding a small handkerchief"></div>

    <h1 class="headline">
      <span class="word-big word-one">ONE</span>
      <span class="word-small word-step">step</span>
      <span class="word-small word-ata">at a</span>
      <span class="word-big word-time">TIME</span>
    </h1>

    <p class="message">
      If you're looking for extra support and guidance<br>
      through a challenging situation<br>
      or you're just ready to move in a new direction in your life,
      <span class="pledge">I look forward to working with you</span>
      <span class="goal">to achieve your goals</span>
    </p>
  </main>
</body>
</html>
```